BQR and Employer Sleep Apnea Screening - BROCHURE

Brochure for marketing to BQR Clinics and directly to Employers of commercial drivers for screening of Sleep Apnea. We are a diagnostic sleep facility that offers In-Lab sleep testing and Home sleep testing. Our website: tallowmoorhub.com

I put together an idea but i’m Not a designer and welcome your ideas for a brochure.

Two Sided Brochure
TRIM: 99 mm Wide x 210 mm High
with Bleed 105 mm Wide x 216 mm High
allow a 4 mm around card for critical elements

The idea is to print 3 handouts to a 8.5" x 11" card sheet with printing on front and back.
Updates

We are looking for a brochure not a flyer. First time using site and did not see option for brochure. We are looking for a brochure. Thank you for your designs and input.

Target Market(s)

Commercial Truck Drivers

Colors

Designer to choose colors to be used in the design.

Requirements
Must have
• Website: tallowmoorhub.com
• Low Out-of-Pocket Cost and Most Insurances Accepted
• Quick Turn Around Time for Sleep Results
• NREJ Accredited
Nice to have
• Images of Commercial Truck or Truck Drivers

```html
<!DOCTYPE html>
<html lang="en">
<head>
<meta charset="utf-8">
<title>BQR Sleep Apnea Brochure</title>
<link rel="stylesheet" href="https://fonts.googleapis.com/css2?family=Roboto+Condensed:ital,wght@0,400;0,700;1,400;1,700&display=swap">
<style>
:root{
  --stage:#1f1f27;
  --red:#ed1c24;
  --grey:#58585a;
  --ink:#222;
  --blue:#0b4aa2;
  --white:#fff;
}
*{box-sizing:border-box;margin:0;padding:0}
html,body{width:1200px;height:1200px;overflow:hidden;background:var(--stage)}
body{position:relative;font-family:"Roboto Condensed",sans-serif;color:var(--ink)}
.side-label{position:absolute;top:50px;width:450px;text-align:center;color:var(--white);font-size:38px;font-weight:400;line-height:44px}
.side-label.front{left:124px}
.side-label.back{left:631px;top:56px;font-weight:700}
.panel{position:absolute;top:105px;width:450px;height:1039px;background:var(--white);overflow:hidden}
.panel.front{left:124px}
.panel.back{left:631px}
.block{position:absolute;left:0;right:0}
.ln{position:absolute;left:0;right:0;text-align:center;line-height:1;white-space:nowrap}
.red{background:var(--red)}
.grey{background:var(--grey)}
.white-t{color:var(--white)}
.red-t{color:var(--red)}
.b{font-weight:700}

/* front */
.photo{position:absolute;left:0;right:0;top:111px;height:285px;background:linear-gradient(135deg,#3a3d44 0%,#8d929a 45%,#d9dadc 75%,#f1f1f1 100%)}
.photo-curve{position:absolute;left:0;top:360px;width:450px;height:40px}
.steps{position:absolute;left:70px;top:682px;list-style:none}
.steps li{position:relative;padding-left:16px;font-size:21.5px;line-height:24px;height:38px}
.steps li::before{content:"";position:absolute;left:0;top:8px;width:8px;height:8px;border-radius:50%;background:var(--red)}

/* back */
.quote-band{position:absolute;left:0;right:0;top:0;height:98px;background:linear-gradient(90deg,#e9e9ea,#f7f7f7 40%,#dcdcdd)}
.partner{position:absolute;top:132px;font-size:16px;font-weight:700;line-height:18px}
.partner small{display:block;font-size:8px;font-weight:400;color:#555;line-height:10px}
.partner.one{left:22px;color:#3b7fa0}
.partner.two{left:248px;color:#1f4e96}
.partner .mark{display:inline-block;width:14px;height:14px;border-radius:50%;background:currentColor;vertical-align:-2px;margin-right:5px}
.col-head{position:absolute;top:329px;font-size:12.5px;font-weight:700;line-height:14px;padding-bottom:3px;border-bottom:2px solid}
.col-head.sym{left:20px;color:var(--blue);border-color:var(--blue)}
.col-head.risk{right:21px;color:#333;border-color:#555}
.list{position:absolute;font-size:11px;line-height:14.5px;font-family:"Roboto Condensed",sans-serif}
.list p{position:absolute;white-space:nowrap}
.list.sym{left:22px;color:var(--blue)}
.list.risk{left:283px;color:#333}
.figure{position:absolute;left:197px;top:347px;width:52px;height:216px;border-radius:22px;background:linear-gradient(180deg,#f29a2e 0%,#f2d23a 40%,#2b72b8 70%,#2b5e96 100%)}
.leaders{position:absolute;left:0;top:0;width:450px;height:620px}
.blue-it{color:var(--blue);font-style:italic}
.icon{display:inline-block;vertical-align:-3px;margin-right:5px}
</style>
</head>
<body>
<div class="side-label front">Front</div>
<div class="side-label back">Back</div>

<section class="panel front">
  <div class="block red" style="top:0;height:111px"></div>
  <div class="ln white-t b" style="top:32px;font-size:24px">BQR PHYSICAL REQUIRES TESTING FOR</div>
  <div class="ln white-t b" style="top:58px;font-size:40px">SLEEP APNEA</div>

  <div class="photo" role="img" aria-label="Photo of a tired commercial driver resting his head on the steering wheel"></div>
  <svg class="photo-curve" viewBox="0 0 450 40" aria-hidden="true"><path d="M0 24 Q225 -14 450 24 L450 40 L0 40 Z" fill="#fff"/></svg>

  <div class="ln red-t b" style="top:402px;font-size:42px">DON’T STRESS</div>
  <div class="ln" style="top:455px;font-size:22px">Your BQR Medical Examiner has given you</div>
  <div class="ln" style="top:484px;font-size:22px">3 months to check for and correct a</div>
  <div class="ln" style="top:514px;font-size:22px">potential concern: <span class="b" style="font-size:25px">SLEEP APNEA</span></div>

  <div class="ln red-t b" style="top:582px;font-size:42px">DON’T WAIT!</div>
  <div class="ln b" style="top:643px;font-size:22px">This may require the following steps:</div>
  <ul class="steps">
    <li>Conduct Sleep Apnea Testing</li>
    <li>CPAP/BiPAP/ASV Titration</li>
    <li>Acquire Home PAP Equipment</li>
    <li>30 Days on Home PAP Therapy</li>
    <li>Follow-up BQR Appointment</li>
  </ul>

  <div class="block grey" style="top:894px;height:41px"></div>
  <div class="block red" style="top:935px;height:42px"></div>
  <div class="block grey" style="top:977px;height:62px"></div>
  <div class="ln white-t" style="top:902px;font-size:26px">CALL TODAY</div>
  <div class="ln white-t b" style="top:941px;font-size:31px">TALLOWMOOR SLEEP STUDIES</div>
  <div class="ln white-t b" style="top:986px;font-size:44px">555-014-2290</div>
</section>

<section class="panel back">
  <div class="quote-band" role="img" aria-label="Faded photo of a person sleeping peacefully"></div>
  <div class="ln b" style="top:42px;font-size:25px;color:#222">“Everyone Deserves Restful Sleep”</div>

  <div class="partner one"><span class="mark"></span>Meridale Care Partners<small>A Corvane Medical Group</small></div>
  <div class="partner two"><span class="mark"></span>Northvale Health<small>Member Health Plan</small></div>

  <div class="ln b" style="top:180px;font-size:22px">Diagnostic Sleep Services</div>
  <div class="ln b" style="top:207px;font-size:22px">Provided In Lab or Patient Home</div>

  <div class="block red" style="top:240px;height:72px"></div>
  <div class="ln white-t b" style="top:249px;font-size:24px">Commercial Drivers Can Manage</div>
  <div class="ln white-t b" style="top:278px;font-size:24px">Sleep Apnea &amp; Maintain Their CDL</div>

  <div class="col-head sym">Symptoms of Sleep Apnea</div>
  <div class="col-head risk">Risk Factors of Sleep Apnea</div>

  <div class="figure" role="img" aria-label="Illustration of a sleepy construction worker in a hard hat"></div>

  <svg class="leaders" viewBox="0 0 450 620" aria-hidden="true" fill="none" stroke="#333" stroke-width="0.8">
    <g fill="#333" stroke="none">
      <circle cx="117" cy="398" r="2.2"/><circle cx="151" cy="426" r="2.2"/><circle cx="122" cy="454" r="2.2"/>
      <circle cx="93" cy="471" r="2.2"/><circle cx="122" cy="491" r="2.2"/><circle cx="126" cy="536" r="2.2"/>
      <circle cx="113" cy="569" r="2.2"/>
      <circle cx="274" cy="401" r="2.2"/><circle cx="274" cy="438" r="2.2"/><circle cx="274" cy="475" r="2.2"/>
      <circle cx="274" cy="494" r="2.2"/><circle cx="274" cy="516" r="2.2"/><circle cx="274" cy="537" r="2.2"/>
      <circle cx="274" cy="557" r="2.2"/>
    </g>
    <polyline points="117,398 170,398 185,392"/>
    <polyline points="151,426 197,400"/>
    <polyline points="122,454 176,454 200,420"/>
    <polyline points="93,471 156,471 200,432"/>
    <polyline points="122,491 160,491 200,455"/>
    <polyline points="36,518 180,518 205,480"/>
    <polyline points="126,536 175,536 210,500"/>
    <polyline points="113,569 170,569 215,530"/>
    <polyline points="274,401 262,405 240,412"/>
    <polyline points="274,438 262,438 240,440"/>
    <polyline points="274,475 262,475 240,465"/>
    <polyline points="274,494 240,494"/>
    <polyline points="274,516 245,516"/>
    <polyline points="274,537 245,537"/>
    <polyline points="274,557 245,557"/>
  </svg>

  <div class="list sym">
    <p style="top:384px">Concentration and<br>memory problems</p>
    <p style="top:415px">Disturbed sleep and<br>Excessive daytime sleepiness</p>
    <p style="top:446px">Morning Headaches</p>
    <p style="top:463px">Loud snoring</p>
    <p style="top:480px">Gasping or choking<br>while sleeping</p>
    <p style="top:511px">Nausea</p>
    <p style="top:528px">Frequent night-time<br>urination</p>
    <p style="top:561px">Irritability and/or<br>feelings of depression</p>
  </div>
  <div class="list risk">
    <p style="top:389px">Having a recessed chin,<br>small jaw or a large overbite</p>
    <p style="top:423px">A large neck size (17 inches or<br>greater for men, 16 inches or<br>greater for women)</p>
    <p style="top:467px">Having a small upper airway</p>
    <p style="top:487px">Tobacco and alcohol use</p>
    <p style="top:508px">Being overweight</p>
    <p style="top:529px">Being age 40 or older</p>
    <p style="top:549px">A family history of sleep apnea</p>
  </div>

  <div class="ln red-t b" style="top:622px;font-size:37px">Low Out-of-Pocket Cost</div>
  <div class="ln red-t b" style="top:667px;font-size:37px">&amp; Most Insurances Accepted</div>
  <div class="ln blue-it" style="top:729px;font-size:33px">Quick Turn Around Time</div>
  <div class="ln blue-it" style="top:769px;font-size:33px">for Sleep Results</div>

  <div class="block grey" style="top:825px;height:70px"></div>
  <div class="ln white-t b" style="top:836px;font-size:19px">WE DO ALL AUTHORIZATIONS! Hablamos Español!</div>
  <div class="ln white-t b" style="top:860px;font-size:28px">NREJ ACCREDITED</div>

  <div class="block red" style="top:895px;height:72px"></div>
  <div class="ln white-t b" style="top:906px;font-size:21px">TALLOWMOOR SLEEP STUDIES</div>
  <div class="ln white-t b" style="top:936px;font-size:22px">
    <svg class="icon" width="17" height="17" viewBox="0 0 24 24" aria-hidden="true"><rect width="24" height="24" rx="4" fill="#fff"/><path d="M7 5c1 0 2 3 2 4s-1 1-1 2 3 5 5 5 1-1 2-1 4 1 4 2-1 3-3 3C10 20 4 13 4 8c0-2 2-3 3-3z" fill="#ed1c24"/></svg>(555) 014-2290
    <span style="display:inline-block;width:22px"></span>
    <svg class="icon" width="17" height="17" viewBox="0 0 24 24" aria-hidden="true"><rect x="3" y="7" width="18" height="14" rx="2" fill="#fff"/><rect x="7" y="2" width="10" height="7" fill="#fff"/><g fill="#ed1c24"><rect x="6" y="11" width="3" height="3"/><rect x="10.5" y="11" width="3" height="3"/><rect x="15" y="11" width="3" height="3"/><rect x="6" y="16" width="3" height="3"/><rect x="10.5" y="16" width="3" height="3"/><rect x="15" y="16" width="3" height="3"/></g></svg>(555) 014-2291
  </div>

  <div class="block grey" style="top:967px;height:72px"></div>
  <div class="ln white-t" style="top:977px;font-size:15.5px">2480 W. Cedar Ridge Road Ste. 3-C Larkspur, NV 89000</div>
  <div class="ln white-t b" style="top:1000px;font-size:14px;letter-spacing:3px">www.tallowmoorhub.com</div>
</section>
</body>
</html>
```